Clearstep Podiatry Care Advertisement Sandwich board

We need a Sandwich board design for our fungal nail clinic - please find attached the sandwich board dimensions.

The sandwich board itself will be displayed outside of a large health clinic and we need it to attract the attention of people walking by. We need a brochure holder included in the design which will hold our brochures which provides as clients with more information (please see attached also).

We are open to the designers creativity but we would like a similar theme portrayed on our board that is similar to our website (www.clearsteppodiatrycare.co.nz) and brochure that incorporates our logo which I have attached). The final design should communicate professionalism and be a minimalist look but modern to capture the attention of pedestrians.

Finally, we would like the website and phone number (07) 382 5164.

We look forward to seeing your work.

```html
<!DOCTYPE html>
<html lang="en">
<head>
<meta charset="utf-8">
<title>Clearstep Podiatry Care – Sandwich Board</title>
<link href="https://fonts.googleapis.com/css2?family=Montserrat:wght@400;600;800;900&family=Oswald:wght@600&family=Cormorant+SC:wght@600&display=swap" rel="stylesheet">
<style>
  :root {
    --blue: #3f63b5;
    --ink: #4a4a4d;
    --body: #55565a;
    --line: #a9c3e6;
    --paper: #ffffff;
    --backdrop: #6380b8;
    --skin-light: #fbe9df;
    --skin-mid: #f0cdb9;
  }
  * { margin: 0; padding: 0; box-sizing: border-box; }
  html, body { width: 909px; height: 1200px; overflow: hidden; background: var(--backdrop); }
  .board {
    position: relative; width: 909px; height: 1200px;
    background: var(--paper); font-family: "Montserrat", sans-serif; color: var(--body);
    overflow: hidden;
  }
  .board__panel {
    position: absolute; left: 0; top: 0; width: 909px; height: 1140px;
    border: 1.5px solid var(--line); border-top: none; border-radius: 22px 22px 22px 22px;
  }
  .board__foot-rail { position: absolute; top: 1140px; bottom: 0; width: 1.5px; background: var(--line); }
  .board__foot-rail--left { left: 41px; }
  .board__foot-rail--right { left: 867px; }
  .brochure-slot {
    position: absolute; left: 360px; top: 39px; width: 188px; height: 36px;
    border: 1.5px solid #dfe3ea; border-radius: 18px;
  }
  .photo-legs {
    position: absolute; left: 323px; top: 105px; width: 586px; height: 898px;
    background: radial-gradient(ellipse 40% 55% at 55% 45%, var(--skin-mid), var(--skin-light) 60%, rgba(255,255,255,0) 85%);
  }
  .brand { position: absolute; left: 40px; top: 50px; width: 250px; text-align: center; }
  .brand__dot { width: 74px; height: 74px; border-radius: 50%; background: var(--blue); margin: 0 auto 14px; }
  .brand__name { font-family: "Montserrat", sans-serif; font-weight: 600; font-size: 17px; letter-spacing: 1.5px; color: var(--ink); text-transform: uppercase; line-height: 1.25; }
  .headline { position: absolute; left: 46px; top: 206px; font-weight: 900; font-size: 70px; line-height: 74px; letter-spacing: -1.5px; }
  .headline__top { color: var(--ink); display: block; }
  .headline__bottom { color: var(--blue); display: block; }
  .intro { position: absolute; left: 48px; top: 378px; width: 440px; font-size: 16px; line-height: 21px; }
  .section-title {
    position: absolute; left: 46px; font-weight: 600; font-size: 26px; color: var(--blue);
    padding-bottom: 2px; border-bottom: 2px solid var(--blue);
  }
  .section-title--treatments { top: 448px; }
  .section-title--tech { top: 720px; }
  .list { position: absolute; left: 48px; list-style: none; font-size: 16px; line-height: 27px; }
  .list--treatments { top: 480px; }
  .list--tech { top: 756px; line-height: 21px; }
  .list__item { position: relative; padding-left: 26px; }
  .list--tech .list__item { margin-bottom: 10px; }
  .list__icon { position: absolute; left: 0; top: 6px; width: 17px; height: 17px; border-radius: 50%; background: var(--blue); }
  .list__tick { position: absolute; left: 0; top: 3px; width: 18px; height: 16px; }
  .tagline {
    position: absolute; left: 48px; top: 1044px; font-family: "Oswald", sans-serif; font-weight: 600;
    font-size: 35px; line-height: 38px; color: var(--blue); transform: scaleY(1.05);
  }
  .divider { position: absolute; left: 504px; top: 1031px; width: 2px; height: 90px; background: var(--blue); }
  .contact { position: absolute; left: 534px; top: 1034px; list-style: none; font-size: 15px; line-height: 24px; color: var(--blue); font-weight: 600; }
  .contact__item { display: flex; align-items: center; gap: 8px; }
  .contact__icon { width: 14px; height: 14px; flex: none; }
</style>
</head>
<body>
<main class="board">
  <div class="board__panel"></div>
  <div class="board__foot-rail board__foot-rail--left"></div>
  <div class="board__foot-rail board__foot-rail--right"></div>
  <div class="brochure-slot"></div>

  <div class="photo-legs" role="img" aria-label="Photograph of smooth bare legs and feet standing on tiptoe, a hand resting on one calf"></div>

  <header class="brand">
    <div class="brand__dot"></div>
    <p class="brand__name">Clearstep<br>Podiatry Care</p>
  </header>

  <h1 class="headline"><span class="headline__top">Your Fungal</span><span class="headline__bottom">Nail Experts</span></h1>

  <p class="intro">We are your experts in foot health with the most comprehensive treatment programme for fungal nail infections including the Lumora Cold Laser</p>

  <h2 class="section-title section-title--treatments">Treatments offered</h2>
  <ul class="list list--treatments">
    <li class="list__item"><span class="list__icon"></span>Definitive diagnosis</li>
    <li class="list__item"><span class="list__icon"></span>Tailored prevention and hygiene<br>strategies</li>
    <li class="list__item"><span class="list__icon"></span>Topical</li>
    <li class="list__item"><span class="list__icon"></span>Oral</li>
    <li class="list__item"><span class="list__icon"></span>Surgical</li>
    <li class="list__item"><span class="list__icon"></span>Cold laser</li>
    <li class="list__item"><span class="list__icon"></span>Combination therapy</li>
  </ul>

  <h2 class="section-title section-title--tech">Latest Technology</h2>
  <ul class="list list--tech">
    <li class="list__item"><svg class="list__tick" viewBox="0 0 18 16"><path d="M2 8l5 5 9-11" fill="none" stroke="#3f63b5" stroke-width="3"/></svg>Cold Laser therapy</li>
    <li class="list__item"><svg class="list__tick" viewBox="0 0 18 16"><path d="M2 8l5 5 9-11" fill="none" stroke="#3f63b5" stroke-width="3"/></svg>Pain Free</li>
    <li class="list__item"><svg class="list__tick" viewBox="0 0 18 16"><path d="M2 8l5 5 9-11" fill="none" stroke="#3f63b5" stroke-width="3"/></svg>Safe, simple and effective</li>
    <li class="list__item"><svg class="list__tick" viewBox="0 0 18 16"><path d="M2 8l5 5 9-11" fill="none" stroke="#3f63b5" stroke-width="3"/></svg>87% Success rates for<br>treating fungal nail<br>infections</li>
    <li class="list__item"><svg class="list__tick" viewBox="0 0 18 16"><path d="M2 8l5 5 9-11" fill="none" stroke="#3f63b5" stroke-width="3"/></svg>Exclusive to Clearstep<br>Podiatry Care</li>
  </ul>

  <p class="tagline">Explore our website to discover<br>your fungal nail solution</p>
  <div class="divider"></div>

  <ul class="contact">
    <li class="contact__item"><svg class="contact__icon" viewBox="0 0 14 14"><rect x="1" y="1" width="12" height="12" rx="2" fill="#3f63b5"/><path d="M4 4c0 4 2 6 6 6l0-2-2-1-1 1c-1-.5-1.5-1-2-2l1-1-1-2z" fill="#fff"/></svg>(07) 382 5164</li>
    <li class="contact__item"><svg class="contact__icon" viewBox="0 0 14 14"><rect x="1" y="3" width="12" height="9" rx="1" fill="#3f63b5"/><path d="M1.5 3.5l5.5 4.5 5.5-4.5" fill="none" stroke="#fff" stroke-width="1.2"/></svg>reception@clearsteppodiatrycare.co.nz</li>
    <li class="contact__item"><svg class="contact__icon" viewBox="0 0 14 14"><circle cx="7" cy="7" r="6" fill="#3f63b5"/><path d="M1 7h12M7 1c-3 3-3 9 0 12M7 1c3 3 3 9 0 12" fill="none" stroke="#fff" stroke-width="1"/></svg>www.clearsteppodiatrycare.co.nz</li>
    <li class="contact__item"><svg class="contact__icon" viewBox="0 0 14 14"><path d="M7 1a4 4 0 0 0-4 4c0 3 4 8 4 8s4-5 4-8a4 4 0 0 0-4-4z" fill="#3f63b5"/><circle cx="7" cy="5" r="1.5" fill="#fff"/></svg>Kowhai Health Pharmacy, Hamilton</li>
  </ul>
</main>
</body>
</html>
```